We need your help in designing the graphical look of the home page of our web site: Plimora.com.

Plimora is an FREE online service that brings consumers and service providers together through online reservations.

Our service is in fact a web application (similar to quindle planner), so we will be using forms, widgets, menus and standard web controls (buttons, fields, links, etc). We need a design that will be easy to integrate with our programming.

This design project is for the HOME page, but we will choose the designer that will design the web page in photoshop in layers, so we can easily derive our other secondary pages ourselves.

If you have any questions please send us a message and we will gladly update the brief with a response.

Happy Designing!
Updates

Hi all, the menu on the home page should be something standard, like: Pricing, features, how it works.

once a user is logged in, they will see their toolbox at all times:
- My Box (links to their main page of bookings)
- My Faborites (view favorite businesses and book quickly with them)
- Settings (set parameters of their account)

There should be a My Profile page as well. 

Thanks!

Reason: I have extended the deadline to receive more designs.

Hi All,

UPDATE: we changed our vision of the home page to have a much simpler design.  something along the lines of chatterloom peeplark and crew lattice.

HOME PAGE:
light colors with white background.  simple, simple, simple!

header should not be big, logo, change language link. try with search bar (what and where).

body should be simple, with an image + register form only.

footer with links to pages for more info:
- Privacy,
- Getting started
- How it works
- Contact us
- FAQ
- Pricing

LOGGED IN PAGE:
when logged in, the header can be the same or reduced to maximize the "working area" (body).
body can be a 2 or 3 column design, as we have a main working area.  in your design, show a calendar.  we need a toolbar (side or top) that will have these buttons, links: MyBox, My Favorites, Settings, My Profile.
We need a section that will display latest messages or notifications.
keep the footer with the links.

Thank you all.

Reason: Holidays

Reason: holidays... lets spend time with our families!

Target Market(s)

Young and mobile consumers + professionals, businesses, restaurants and commerces wishing to offer online reservations (appointments and reservations)

Industry/Entity Type

Quindle

Requirements
Must have
• - Easy to integrate with web programming
- light weight visual design. We want something with light tone colors as background
- home page will have a content slider that will show some catch phrases.
- Overall design should be more on the "cartoony" side. Should give a casual, humour and friendly ambiance.

The home page should have these sections:
- a search section for consumers to find local businesses. They will search by specifying "What?" & "Where?"
- a content slider that will cycle through catch phrases and features. Each pane should have an image representative of the text.
- have 4 highlighted sections
- Plimora is great for (list of different businesses types that use plimora)
- Plimora is available for FREE to everyone
- Main features list (accept 24/7 reservations, never reveal your schedule, automatic reminders, marketing campaigns)
- The more you plim, the more you save! (info on our loyalty program that entitles consumers to greater savings and benefits).

One a user logs in, all the certer page info will be replaced by a content div that will allow content to display based on selected menu item
- My Box (opens the main section where all happens. This section should have a design that gives the impression that we're looking in a box)
- My Profile
- My Favorites
Should not have
• - Don't use actual photos of real people, rather opt for sketches and cartoony characters.

```html
<!DOCTYPE html>
<html lang="en">
<head>
<meta charset="utf-8">
<title>Plimora – Online Reservation</title>
<link href="https://fonts.googleapis.com/css2?family=Arimo:wght@400;700&display=swap" rel="stylesheet">
<style>
:root{
  --header-bg:#1c1c1c;
  --header-edge:#3a3a3a;
  --hero-bg:#e4f1f2;
  --hero-edge:#c9d8da;
  --title:#3f6a89;
  --muted:#8fb3c6;
  --field-bg:#f3f5f5;
  --field-border:#8a9aa6;
  --text:#2b3a44;
  --link:#3a6a86;
  --sign-in:#1aa3d9;
  --icon-bg:#b9d4d6;
  --icon-fg:#3a3f42;
  --gold-top:#efe6b6;
  --gold-bottom:#c9b575;
  --lime-top:#e9f88a;
  --lime-bottom:#b5d61f;
  --white:#ffffff;
}
*{box-sizing:border-box;margin:0;padding:0}
html,body{width:1200px;height:589px;overflow:hidden;background:var(--white);font-family:"Arimo",Arial,sans-serif;color:var(--text)}
.page{position:relative;width:1200px;height:589px}
.abs{position:absolute}

.site-header{left:0;top:0;width:1200px;height:70px;background:linear-gradient(#2a2a2a,#161616);border-bottom:2px solid var(--header-edge)}
.brand{left:59px;top:22px;display:flex;align-items:center;gap:10px;color:var(--white);font-weight:700;font-size:19px;letter-spacing:1px}
.brand-mark{width:26px;height:26px;background:#2a96b4;border-radius:3px}
.tagline{left:365px;top:28px;color:#5c5c5c;font-weight:700;font-size:15px}
.search-label{top:8px;color:var(--white);font-size:11px;font-weight:700}
.search-field{top:26px;width:228px;height:23px;background:#ecebea;border:1px solid #777;font-size:11px;color:#555;padding:4px 8px}
.search-button{left:1052px;top:24px;width:91px;height:26px;border-radius:4px;background:linear-gradient(var(--gold-top),var(--gold-bottom));border:1px solid #8b7c44;font-size:15px;color:#222;text-align:center;line-height:24px}

.hero{left:0;top:72px;width:1200px;height:369px;background:var(--hero-bg);border-bottom:1px solid var(--hero-edge)}
.hero-badge{left:111px;top:150px;width:160px;height:160px;border-radius:50%;background:var(--white);border:2px solid #d3e2e4;box-shadow:0 2px 6px rgba(0,0,0,.12);display:flex;align-items:center;justify-content:center;color:#2a96b4;font-weight:700;font-size:20px}
.hero-title{left:306px;top:162px;font-size:23px;font-weight:700;color:var(--title)}
.hero-text{left:306px;top:197px;width:400px;font-size:16px;line-height:27px;color:var(--muted)}
.feature-icons{left:303px;top:265px;display:flex;gap:15px}
.feature-icon{width:40px;height:40px;border-radius:50%;background:var(--icon-bg);border:1px solid #a5c3c6;display:flex;align-items:center;justify-content:center}

.register-title{left:812px;top:110px;font-size:21px;font-weight:700;color:var(--title)}
.rule{left:812px;width:227px;height:1px;background:#c3d3d6}
.register-note{left:812px;top:160px;font-size:11px;color:var(--muted)}
.register-field{left:812px;width:227px;height:29px;background:var(--field-bg);border:2px solid var(--field-border);font-size:16px;color:#333;padding:3px 11px}
.join-button{left:812px;top:302px;width:111px;height:35px;border-radius:6px;background:linear-gradient(var(--lime-top),var(--lime-bottom));border:1px solid #8faa1a;box-shadow:0 2px 3px rgba(0,0,0,.2);font-size:16px;font-weight:700;color:#26340a;text-align:center;line-height:33px}
.member-line{left:812px;top:368px;font-size:12px;color:var(--link)}
.member-line a{color:var(--sign-in);margin-left:14px;text-decoration:underline}

.language{left:57px;top:456px;width:88px;height:24px;border:1px solid #9aa8b0;background:linear-gradient(#fff,#e9eef0);font-size:13px;padding:4px 11px;color:#333}
.language-caret{position:absolute;right:8px;top:8px;border-left:6px solid transparent;border-right:6px solid transparent;border-top:7px solid var(--link)}
.footer-links{left:168px;top:459px;display:flex;gap:18px;font-size:14px;color:var(--link)}
.follow{left:826px;top:458px;display:flex;align-items:center;gap:10px;font-size:12px;color:var(--link)}
.follow strong{font-size:16px;color:var(--title)}
.social{display:flex;align-items:center;gap:4px}
.social i{width:10px;height:10px;background:var(--title);display:inline-block}
</style>
</head>
<body>
<div class="page">
  <header class="site-header abs">
    <div class="brand abs"><span class="brand-mark"></span>Plimora</div>
    <div class="tagline abs">Make a FREE reservation</div>
    <div class="search-label abs" style="left:573px">What</div>
    <div class="search-field abs" style="left:571px">e.g. Italian food, XXXX film</div>
    <div class="search-label abs" style="left:814px">Where</div>
    <div class="search-field abs" style="left:812px">e.g. Some Neighborhood</div>
    <div class="search-button abs">Search</div>
  </header>

  <section class="hero abs"></section>
  <div class="hero-badge abs">Plimora</div>
  <h1 class="hero-title abs">Online Reservation</h1>
  <p class="hero-text abs">Mattis, risus aliquam cum a, pulvinar platea pulvinar risus pulvinar odio lundium dis nec sagittis eu mid</p>
  <div class="feature-icons abs">
    <span class="feature-icon"><svg width="24" height="24" viewBox="0 0 24 24"><path d="M9 5l11-2v13" stroke="#3a3f42" stroke-width="2.5" fill="none"/><circle cx="6" cy="18" r="3.5" fill="#3a3f42"/><circle cx="17" cy="16" r="3.5" fill="#3a3f42"/><path d="M9 5v13" stroke="#3a3f42" stroke-width="2.5"/></svg></span>
    <span class="feature-icon"><svg width="24" height="24" viewBox="0 0 24 24"><path d="M12 2a7 7 0 0 0-4 12.7V17h8v-2.3A7 7 0 0 0 12 2z" fill="#3a3f42"/><rect x="9" y="18.5" width="6" height="3" rx="1" fill="#3a3f42"/></svg></span>
    <span class="feature-icon"><svg width="24" height="24" viewBox="0 0 24 24"><text x="12" y="20" text-anchor="middle" font-family="Arimo,Arial,sans-serif" font-weight="700" font-size="22" fill="#3a3f42">$</text></svg></span>
    <span class="feature-icon"><svg width="24" height="24" viewBox="0 0 24 24"><path d="M2 13l8-2 5-8h2l-2 8 6 0 2-3h2l-1 5 1 5h-2l-2-3h-6l2 8h-2l-5-8-8-2z" fill="#3a3f42"/></svg></span>
    <span class="feature-icon"><svg width="24" height="24" viewBox="0 0 24 24"><circle cx="12" cy="12" r="10" fill="#3a3f42"/><path d="M12 5v7l5 3" stroke="#fff" stroke-width="2" fill="none"/></svg></span>
  </div>

  <h2 class="register-title abs">Register</h2>
  <div class="rule abs" style="top:145px"></div>
  <p class="register-note abs">Plimora is available for FREE to everyone</p>
  <div class="register-field abs" style="top:181px">Your Name</div>
  <div class="register-field abs" style="top:221px">Email</div>
  <div class="register-field abs" style="top:260px">Password</div>
  <div class="join-button abs">Join Now !</div>
  <div class="rule abs" style="top:354px"></div>
  <p class="member-line abs">Already a Plimora member? <a>Sign In »</a></p>

  <footer>
    <div class="language abs">English<span class="language-caret"></span></div>
    <nav class="footer-links abs"><span>Privacy</span><span>Getting Started</span><span>How It Works</span><span>Contact Us</span><span>FAQ</span><span>Pricing</span></nav>
    <div class="follow abs"><strong>Follow Us:</strong>
      <span class="social"><i></i>chatterloom</span>
      <span class="social"><i></i>peeplark</span>
      <span class="social"><i></i>Quindle</span>
    </div>
  </footer>
</div>
</body>
</html>
```